Bellamy’s Pool Fencinf

We need to add the logo, front back and sides, we need to add phone number.
Call Us Now
725-341-8846
Mesh Pool Fencing
Glass Pool Fencing
Family owned and operated

Our Legacy is Your Family’s Safety

Torvane 2500 Hauler Cargo Van

As Seen On TV

Www.BellamysPoolFencing.example

```html
<!DOCTYPE html>
<html lang="en">
<head>
<meta charset="utf-8">
<title>Bellamy’s Pool Fencinf – Van Wrap</title>
<link rel="stylesheet" href="https://fonts.googleapis.com/css2?family=Fredoka:wght@600&family=Oswald:wght@500&family=Poppins:wght@600;700&display=swap">
<style>
  :root{
    --bg:#ffffff;
    --body:#eef0f2;
    --body-shade:#d9dde1;
    --pool:#1e9fe0;
    --pool-deep:#0c6fb8;
    --pool-light:#7fd0f5;
    --sun:#f0b519;
    --ink:#1f2a33;
    --brand:#1a8fd6;
    --glass:#16191c;
    --tyre:#202326;
    --rim:#b9bec3;
    --line:#b7bcc1;
  }
  html,body{margin:0;padding:0;width:1200px;height:1200px;overflow:hidden;background:var(--bg);}
  .canvas{display:block;width:1200px;height:1200px;}
  .van-body{fill:var(--body);stroke:var(--body-shade);stroke-width:2;}
  .door-seam{fill:none;stroke:var(--line);stroke-width:2;}
  .handle{fill:#3b4147;}
  .window{fill:var(--glass);}
  .bumper{fill:#2a2e32;}
  .tyre{fill:var(--tyre);}
  .rim{fill:var(--rim);stroke:#8d9398;stroke-width:3;}
  .hub{fill:#6d7378;}
  .light-rear{fill:#c4262e;}
  .light-front{fill:#e08a1e;}
  .accent-stripe{fill:var(--sun);}
  .brand-name{font-family:"Fredoka",sans-serif;font-weight:600;font-size:30px;fill:var(--brand);}
  .services{font-family:"Oswald",sans-serif;font-weight:500;font-size:15px;fill:var(--pool-deep);letter-spacing:.3px;}
  .call-now{font-family:"Poppins",sans-serif;font-weight:600;font-size:14px;fill:var(--sun);}
  .phone{font-family:"Poppins",sans-serif;font-weight:700;font-size:26px;fill:var(--ink);}
  .website{font-family:"Poppins",sans-serif;font-weight:600;font-size:12px;fill:var(--pool-deep);}
  .tagline{font-family:"Oswald",sans-serif;font-weight:500;font-size:17px;fill:var(--ink);letter-spacing:4.5px;}
</style>
</head>
<body>
<svg class="canvas" viewBox="0 0 1200 1200" xmlns="http://www.w3.org/2000/svg">
  <defs>
    <linearGradient id="poolWater" x1="0" y1="0" x2="0" y2="1">
      <stop offset="0" stop-color="#5cc4f2"/>
      <stop offset="1" stop-color="#138ad4"/>
    </linearGradient>
    <linearGradient id="splashWater" x1="0" y1="0" x2="1" y2="1">
      <stop offset="0" stop-color="#bfe7fa"/>
      <stop offset=".5" stop-color="#3fb1ea"/>
      <stop offset="1" stop-color="#0f78c4"/>
    </linearGradient>
    <clipPath id="bodyClip">
      <path d="M102 402 Q104 392 118 392 L800 392 Q840 394 880 440 L905 465 Q1040 505 1098 540 Q1112 552 1112 575 L1112 680 L96 680 Z"/>
    </clipPath>
  </defs>

  <g class="van">
    <path class="van-body" d="M102 402 Q104 392 118 392 L800 392 Q840 394 880 440 L905 465 Q1040 505 1098 540 Q1112 552 1112 575 L1112 680 L96 680 Z"/>

    <g class="wrap-graphics" clip-path="url(#bodyClip)">
      <path role="img" aria-label="Pool water splash with rising bubbles" fill="url(#splashWater)" d="M420 392 L1120 392 L1120 620 Q960 560 900 640 L880 560 Q760 470 660 430 Q560 410 420 392 Z"/>
      <path fill="url(#poolWater)" d="M96 555 Q300 540 420 640 L96 680 Z"/>
      <path fill="url(#poolWater)" d="M96 560 Q330 545 470 650 L470 690 L96 690 Z"/>
      <path class="accent-stripe" d="M96 566 Q260 556 330 572 Q250 566 96 574 Z"/>
      <path class="accent-stripe" d="M330 585 Q420 600 480 640 Q410 608 330 592 Z"/>
    </g>

    <line class="door-seam" x1="425" y1="398" x2="425" y2="680"/>
    <line class="door-seam" x1="545" y1="398" x2="545" y2="680"/>
    <line class="door-seam" x1="685" y1="398" x2="685" y2="680"/>
    <rect class="handle" x="532" y="540" width="6" height="22" rx="2"/>
    <rect class="handle" x="692" y="540" width="6" height="22" rx="2"/>

    <path class="window" d="M712 418 L835 418 Q860 440 880 500 L880 528 L712 528 Z"/>
    <rect class="light-rear" x="115" y="456" width="14" height="60" rx="3"/>
    <rect class="light-front" x="1050" y="590" width="48" height="18" rx="3"/>
    <rect class="bumper" x="90" y="660" width="150" height="30" rx="6"/>
    <rect class="bumper" x="1040" y="640" width="78" height="50" rx="8"/>

    <g class="wheel">
      <circle class="tyre" cx="310" cy="690" r="70"/>
      <circle class="rim" cx="310" cy="690" r="44"/>
      <circle class="hub" cx="310" cy="690" r="12"/>
    </g>
    <g class="wheel">
      <circle class="tyre" cx="940" cy="690" r="70"/>
      <circle class="rim" cx="940" cy="690" r="44"/>
      <circle class="hub" cx="940" cy="690" r="12"/>
    </g>
  </g>

  <g class="brand">
    <text class="brand-name" x="290" y="438" text-anchor="middle">BELLAMY’S POOL</text>
    <text class="brand-name" x="285" y="470" text-anchor="middle">FENCINF</text>
  </g>

  <rect role="img" aria-label="Illustration of a grandmother and two children beside a fenced backyard pool" x="148" y="480" width="270" height="105" rx="40" fill="#9fb3c2"/>

  <g class="services">
    <text x="538" y="590" text-anchor="middle">MESH POOL FENCING • GLASS POOL FENCING</text>
    <text x="538" y="610" text-anchor="middle">FAMILY OWNED AND OPERATED</text>
  </g>

  <g class="contact">
    <text class="call-now" x="872" y="572" text-anchor="end">Call Us Now</text>
    <text class="phone" x="690" y="600">725-341-8846</text>
    <text class="website" x="690" y="620">Www.BellamysPoolFencing.example</text>
  </g>

  <text class="tagline" x="620" y="671" text-anchor="middle">OUR LEGACY IS YOUR FAMILY’S SAFETY</text>
</svg>
</body>
</html>
```